New Corporate Email footer (business card design) for 40th Anniversary for Timber Traders

We are traders in sustainable timber worldwide, specialising in tropical hardwoods.
We need to keep our current company logo, but update our email footer with a business card like design which marks the company's 40th Anniversary. 1981-2021. We would need:
Company Logo, Name and Address, website
Sender's: Name, Tel no, fax no, email address
We would need this in a format which we could update ourselves re names/phone numbers if any change.

Target Market(s)

Customers, suppliers, service providers

Contact Information for Business Card

Maria Denton
Tel: +44 (0) 208 734 2216
Fax: +44 (0) 208 734 5580
Email: maria@pvrwoodline.co.uk
Web: www.pvrwoodline.co.uk

PVR Woodline Ltd. 17 Bramble Court, Ashford Lane, Hollowmere, Surrey KT5 3QW, UNITED KINGDOM

IMPORTANT NOTICE - This message contains confidential information for the intended addressee only. Any views expressed are those of the sender not PVR Woodline Ltd unless otherwise stated. If you receive this message [and any attachment(s)] in error you must not store, copy, disclose or otherwise use any part of it and should advise the sender immediately on 020 8734 9162. Internet communications are not guaranteed secure or virus free. PVR reserves the right to monitor all e-mail communications and does not accept responsibility for any loss or damage resulting from access of this e-mail or any file(s) attached.

Font styles to use
Sans Serif
Other font styles liked:
• not actually sure

Requirements
Must have
• mention of company's 40th Anniversary 1981-2021, which is the whole point of the design
Nice to have
• Our company colour is British Racing Green, but any green theme may be good
Maybe a tree design but allowing the company logo to stand out.

```html
<!DOCTYPE html>
<html lang="en">
<head>
<meta charset="utf-8">
<title>PVR Woodline – 40th Anniversary Email Card</title>
<link href="https://fonts.googleapis.com/css2?family=Montserrat:wght@400;500;600;700&family=Libre+Baskerville&display=swap" rel="stylesheet">
<style>
  :root {
    --racing-green: #2f5a17;
    --paper: #f3f3f1;
    --ink-dark: #1f261c;
    --backdrop: #d9d9d9;
    --on-green: #f2f5ee;
  }
  * { box-sizing: border-box; margin: 0; padding: 0; }
  html, body { width: 1200px; height: 900px; overflow: hidden; }
  body {
    background: var(--backdrop);
    font-family: "Montserrat", sans-serif;
    position: relative;
  }
  .card {
    position: absolute;
    width: 560px;
    height: 320px;
    border-radius: 4px;
    box-shadow: 0 10px 28px rgba(0,0,0,.18);
    overflow: hidden;
  }

  /* Front */
  .card-front { left: 60px; top: 90px; background: var(--racing-green); color: var(--on-green); }
  .year { position: absolute; font-family: "Libre Baskerville", serif; font-size: 24px; }
  .year-start { left: 40px; top: 200px; }
  .year-end { right: 40px; top: 40px; }
  .front-rule-top { position: absolute; left: 330px; right: 40px; top: 120px; border-top: 1px solid rgba(242,245,238,.7); }
  .front-rule-bottom { position: absolute; left: 40px; right: 40px; top: 268px; border-top: 1px solid rgba(242,245,238,.7); }
  .wordmark {
    position: absolute; display: flex; flex-direction: column; align-items: center; gap: 10px;
  }
  .wordmark-dot { border-radius: 50%; }
  .wordmark-name { font-weight: 700; letter-spacing: 2px; }
  .front-mark { left: 50%; top: 36px; transform: translateX(-50%); }
  .front-mark .wordmark-dot { width: 110px; height: 110px; background: var(--on-green); }
  .front-mark .wordmark-name { font-size: 48px; color: var(--on-green); }
  .front-web { position: absolute; left: 0; right: 0; top: 240px; text-align: center; font-size: 17px; font-weight: 500; }
  .front-address { position: absolute; left: 0; right: 0; top: 278px; text-align: center; font-size: 9.5px; letter-spacing: .2px; }

  /* Back */
  .card-back { left: 580px; top: 490px; background: var(--paper); color: var(--racing-green); }
  .corner { position: absolute; background: var(--racing-green); }
  .corner-top-right { right: 0; top: 0; width: 72px; height: 52px; }
  .corner-right { right: 0; top: 150px; width: 44px; height: 60px; }
  .corner-left { left: 0; top: 96px; width: 44px; height: 44px; }
  .corner-bottom-left { left: 0; bottom: 0; width: 44px; height: 60px; }
  .back-mark { left: 70px; top: 40px; }
  .back-mark .wordmark-dot { width: 110px; height: 110px; background: var(--racing-green); }
  .back-mark .wordmark-name { font-size: 48px; color: var(--racing-green); }
  .back-web { position: absolute; left: 62px; top: 250px; font-size: 16px; font-weight: 500; }
  .anniversary-band {
    position: absolute; left: 300px; bottom: 22px; width: 230px; height: 36px;
    background: var(--ink-dark); color: #fff;
    font-family: "Libre Baskerville", serif; font-size: 18px;
    display: flex; align-items: center; justify-content: center;
  }
  .contact { position: absolute; left: 270px; top: 60px; }
  .contact-name { font-size: 24px; font-weight: 600; letter-spacing: 1.5px; margin-bottom: 12px; }
  .contact-list { list-style: none; font-size: 14.5px; font-weight: 500; }
  .contact-list li { display: flex; align-items: center; gap: 10px; margin-bottom: 9px; }
  .contact-list svg { width: 16px; height: 16px; flex: none; }
</style>
</head>
<body>

  <section class="card card-front" aria-label="Card front">
    <span class="year year-end">2021</span>
    <span class="year year-start">1981</span>
    <div class="front-rule-top"></div>
    <div class="wordmark front-mark">
      <span class="wordmark-dot"></span>
      <span class="wordmark-name">PVR</span>
    </div>
    <p class="front-web">www.pvrwoodline.co.uk</p>
    <div class="front-rule-bottom"></div>
    <p class="front-address">PVR Woodline Ltd. 17 Bramble Court, Ashford Lane, Hollowmere, Surrey KT5 3QW, UNITED KINGDOM</p>
  </section>

  <section class="card card-back" aria-label="Card back">
    <div class="corner corner-top-right" role="img" aria-label="Corner decoration"></div>
    <div class="corner corner-right" role="img" aria-label="Edge decoration"></div>
    <div class="corner corner-left" role="img" aria-label="Edge decoration"></div>
    <div class="corner corner-bottom-left" role="img" aria-label="Corner decoration"></div>

    <div class="wordmark back-mark">
      <span class="wordmark-dot"></span>
      <span class="wordmark-name">PVR</span>
    </div>

    <div class="contact">
      <h1 class="contact-name">MARIA DENTON</h1>
      <ul class="contact-list">
        <li>
          <svg viewBox="0 0 16 16" aria-hidden="true"><rect width="16" height="16" rx="3" fill="#2f5a17"/><path d="M5 4l2 2-1 1.3c.6 1.2 1.5 2.1 2.7 2.7L10 9l2 2-1.2 1.2C8 12 4 8 3.8 5.2z" fill="#f3f3f1"/></svg>
          +44 (0) 208 734 2216
        </li>
        <li>
          <svg viewBox="0 0 16 16" aria-hidden="true"><rect x="2" y="5" width="12" height="9" fill="#2f5a17"/><rect x="4" y="2" width="8" height="5" fill="#f3f3f1" stroke="#2f5a17"/><rect x="5" y="9" width="6" height="2" fill="#f3f3f1"/></svg>
          +44 (0) 208 734 5580
        </li>
        <li>
          <svg viewBox="0 0 16 16" aria-hidden="true"><rect x="1" y="3" width="14" height="10" fill="#2f5a17"/><path d="M1 3l7 6 7-6" fill="none" stroke="#f3f3f1" stroke-width="1.4"/></svg>
          maria@pvrwoodline.co.uk
        </li>
      </ul>
    </div>

    <p class="back-web">www.pvrwoodline.co.uk</p>
    <div class="anniversary-band">1981 - 2021</div>
  </section>

</body>
</html>
```